AK MERIDEL BUSINESS CARD DESIGN PROJECT

We need to utilize our logo that was expertly created on Markvelloo and now need to match this with a business card design.

```html
<!DOCTYPE html>
<html lang="en">
<head>
<meta charset="utf-8">
<title>AK MERIDEL Business Card</title>
<link rel="stylesheet" href="https://fonts.googleapis.com/css2?family=Lato:wght@400;700&family=Montserrat:wght@700&display=swap">
<style>
  :root {
    --brand-blue: #1257b0;
    --brand-blue-deep: #0e4a99;
    --paper: #ffffff;
    --ink-grey: #5a5f66;
    --stage: #2c2e31;
  }
  * { margin: 0; padding: 0; box-sizing: border-box; }
  html, body { width: 1200px; height: 952px; overflow: hidden; }
  body {
    background: var(--stage);
    display: flex;
    align-items: center;
    justify-content: center;
    gap: 44px;
    font-family: "Lato", sans-serif;
  }
  .card {
    position: relative;
    width: 520px;
    height: 297px;
    border-radius: 22px;
    overflow: hidden;
  }

  /* Front side */
  .card-front { background: var(--paper); }
  .brand {
    position: absolute;
    top: 52px;
    left: 0;
    right: 0;
    display: flex;
    align-items: center;
    justify-content: center;
    gap: 12px;
  }
  .brand-mark {
    width: 16px;
    height: 16px;
    background: var(--brand-blue);
  }
  .brand-name {
    font-family: "Montserrat", sans-serif;
    font-weight: 700;
    font-size: 30px;
    letter-spacing: 8px;
    color: var(--brand-blue);
  }
  .person {
    position: absolute;
    top: 138px;
    left: 44px;
  }
  .person-name {
    font-size: 17px;
    color: var(--brand-blue);
    letter-spacing: 0.5px;
  }
  .person-name strong { font-weight: 700; }
  .person-role {
    margin-top: 4px;
    font-size: 13px;
    color: var(--ink-grey);
  }
  .contacts {
    position: absolute;
    top: 134px;
    left: 272px;
    list-style: none;
  }
  .contacts li {
    display: flex;
    align-items: center;
    gap: 9px;
    font-size: 12.5px;
    color: var(--ink-grey);
    height: 22px;
  }
  .contacts .icon {
    width: 15px;
    height: 15px;
    border-radius: 3px;
    background: var(--brand-blue);
    display: flex;
    align-items: center;
    justify-content: center;
  }
  .address-band {
    position: absolute;
    left: 0;
    right: 0;
    top: 232px;
    height: 30px;
    background: var(--brand-blue);
    color: var(--paper);
    font-size: 13px;
    letter-spacing: 0.5px;
    display: flex;
    align-items: center;
    padding-left: 44px;
  }

  /* Back side */
  .card-back { background: var(--brand-blue); }
  .back-name {
    position: absolute;
    top: 50%;
    left: 50%;
    transform: translate(-50%, -50%);
    font-family: "Montserrat", sans-serif;
    font-weight: 700;
    font-size: 30px;
    letter-spacing: 10px;
    color: var(--paper);
    white-space: nowrap;
  }
</style>
</head>
<body>

  <section class="card card-front" aria-label="Business card front">
    <div class="brand">
      <span class="brand-mark"></span>
      <span class="brand-name">AK MERIDEL</span>
    </div>

    <div class="person">
      <p class="person-name">DANIEL R. <strong>HARTWELL</strong></p>
      <p class="person-role">Managing Director</p>
    </div>

    <ul class="contacts">
      <li>
        <span class="icon">
          <svg width="9" height="9" viewBox="0 0 24 24" aria-hidden="true"><path fill="#fff" d="M6.6 10.8a15 15 0 0 0 6.6 6.6l2.2-2.2c.3-.3.7-.4 1-.2 1.1.4 2.3.6 3.6.6.6 0 1 .4 1 1V20c0 .6-.4 1-1 1A17 17 0 0 1 3 4c0-.6.4-1 1-1h3.5c.6 0 1 .4 1 1 0 1.3.2 2.5.6 3.6.1.3 0 .7-.2 1z"/></svg>
        </span>
        +00 987 654 32
      </li>
      <li>
        <span class="icon">
          <svg width="10" height="8" viewBox="0 0 20 14" aria-hidden="true"><rect x="1" y="1" width="18" height="12" fill="none" stroke="#fff" stroke-width="2"/><path d="M1 1l9 7 9-7" fill="none" stroke="#fff" stroke-width="2"/></svg>
        </span>
        hello@akmeridel.com
      </li>
      <li>
        <span class="icon">
          <svg width="9" height="9" viewBox="0 0 24 24" aria-hidden="true"><path fill="#fff" d="M12 2l8 20-8-5-8 5z"/></svg>
        </span>
        www.akmeridel.com
      </li>
    </ul>

    <div class="address-band">1207 Harbor Lane Avenue Portland, OR 97204</div>
  </section>

  <section class="card card-back" aria-label="Business card back">
    <span class="back-name">AK MERIDEL</span>
  </section>

</body>
</html>
```